Tavrin Foods Packing 5 to Drive

5 Principals for all the team to follow by!

Please can you convert the 5 to drive "screenshot 2024-09-08" image into something that has a similair look and feel to the Vision and Values style?

```html
<!DOCTYPE html>
<html lang="en">
<head>
<meta charset="utf-8">
<title>The Tavrin Way – Our 5 to Drive</title>
<link href="https://fonts.googleapis.com/css2?family=Montserrat:wght@300;400;800&display=swap" rel="stylesheet">
<style>
  :root {
    --paper: #ffffff;
    --green: #0b622e;
    --gold: #dca71f;
    --mustard: #d8bd5a;
    --teal: #57a0ab;
    --orange: #cd5b27;
    --red: #b52126;
    --navy: #232635;
    --logo-grey: #c4c4c4;
    --frame-grey: #d8d8d8;
    --ink-light: #ffffff;
    --ghost: rgba(255,255,255,0.28);
  }
  * { box-sizing: border-box; margin: 0; padding: 0; }
  html, body { width: 1200px; height: 800px; overflow: hidden; background: var(--paper); }
  body { font-family: "Montserrat", sans-serif; }

  .board { position: relative; width: 1200px; height: 800px; background: var(--paper); }

  .side-band {
    position: absolute; top: 28px; width: 98px; height: 744px;
    background: var(--green); color: var(--gold);
    display: flex; align-items: center; justify-content: center;
    font-weight: 800; font-size: 54px; letter-spacing: 0.5px; white-space: nowrap;
  }
  .side-band span { writing-mode: vertical-rl; line-height: 1; }
  .side-band--left { left: 27px; }
  .side-band--left span { transform: rotate(180deg); }
  .side-band--right { left: 1076px; }

  .tile {
    position: absolute; overflow: hidden; color: var(--ink-light);
    padding: 46px 0 0 52px;
  }
  .tile__title { font-weight: 800; font-size: 46px; line-height: 1.22; position: relative; z-index: 2; }
  .tile__sub { font-weight: 300; font-size: 46px; line-height: 1.2; position: relative; z-index: 2; }
  .tile__sub--small { font-size: 29px; line-height: 1.27; margin-top: 4px; }
  .tile__num {
    position: absolute; left: 52px; bottom: -58px;
    font-weight: 800; font-size: 118px; line-height: 1; color: var(--ghost); z-index: 1;
  }
  .tile__icon { position: absolute; z-index: 1; fill: none; stroke: var(--ghost); stroke-width: 3; stroke-linecap: round; stroke-linejoin: round; }

  .tile--safety  { left: 138px; top: 28px;  width: 363px; height: 239px; background: var(--mustard); }
  .tile--quality { left: 513px; top: 28px;  width: 550px; height: 239px; background: var(--teal); }
  .tile--team    { left: 138px; top: 280px; width: 550px; height: 238px; background: var(--orange); }
  .tile--plan    { left: 700px; top: 280px; width: 363px; height: 238px; background: var(--red); }
  .tile--process { left: 700px; top: 532px; width: 363px; height: 240px; background: var(--navy); }
  .tile--team, .tile--safety, .tile--quality { padding-top: 44px; }
  .tile--plan { padding-top: 50px; }

  .brand-tile {
    position: absolute; left: 138px; top: 532px; width: 550px; height: 240px;
    border: 1.5px solid var(--frame-grey); background: var(--paper);
    display: flex; align-items: center; justify-content: center; gap: 16px;
  }
  .brand-tile__mark { width: 22px; height: 22px; background: var(--logo-grey); }
  .brand-tile__name { font-weight: 800; font-size: 46px; color: var(--logo-grey); letter-spacing: -0.5px; text-transform: uppercase; }
</style>
</head>
<body>
<main class="board">
  <aside class="side-band side-band--left"><span>THE TAVRIN WAY</span></aside>

  <section class="tile tile--safety">
    <svg class="tile__icon" style="left:218px;top:38px" width="120" height="150" viewBox="0 0 120 150">
      <path d="M44 150V95L30 70V30a6 6 0 0 1 12 0v30M42 40V12a6 6 0 0 1 12 0v40M54 22a6 6 0 0 1 12 0v32M66 32a6 6 0 0 1 12 0v40l-8 23v55"/>
      <path d="M6 150V110L0 92V62a5 5 0 0 1 10 0M100 150V110l10-20V62a5 5 0 0 0-10 0"/>
    </svg>
    <h2 class="tile__title">H&amp;S -</h2>
    <p class="tile__sub">Call It Out</p>
    <span class="tile__num">01</span>
  </section>

  <section class="tile tile--quality">
    <svg class="tile__icon" style="left:360px;top:36px" width="130" height="150" viewBox="0 0 130 150">
      <circle cx="65" cy="40" r="30"/><circle cx="65" cy="40" r="20"/>
      <path d="M56 40l7 7 12-13"/>
      <path d="M5 90v40l25 18M125 90v40l-25 18M20 110l25 20M110 110l-25 20"/>
    </svg>
    <h2 class="tile__title">GMP / Quality -</h2>
    <p class="tile__sub">Drive the Standard</p>
    <span class="tile__num">02</span>
  </section>

  <section class="tile tile--team">
    <svg class="tile__icon" style="left:335px;top:36px" width="190" height="160" viewBox="0 0 190 160">
      <circle cx="95" cy="40" r="22"/><circle cx="40" cy="60" r="18"/><circle cx="150" cy="60" r="18"/>
      <circle cx="95" cy="108" r="20"/>
      <path d="M2 135c0-25 15-40 38-40s30 10 30 20M188 135c0-25-15-40-38-40s-30 10-30 20M60 158c0-18 15-28 35-28s35 10 35 28"/>
    </svg>
    <h2 class="tile__title">Team &amp; Behaviors</h2>
    <p class="tile__sub tile__sub--small">What’s Expected of You and<br>Your Team?</p>
    <span class="tile__num">03</span>
  </section>

  <section class="tile tile--plan">
    <svg class="tile__icon" style="left:165px;top:42px" width="160" height="145" viewBox="0 0 160 145">
      <circle cx="130" cy="25" r="20"/>
      <path d="M136 16h-9a5 5 0 0 0 0 10h6a5 5 0 0 1 0 10h-10M130 10v5M130 36v5"/>
      <path d="M5 105l40-20 25 10 50-45M120 50h-12M120 50v12"/>
      <path d="M15 140v-25M35 140v-35M55 140v-28M75 140v-40M95 140v-50M115 140v-70M0 140h160"/>
    </svg>
    <h2 class="tile__title">Plan<br>Attainment</h2>
    <span class="tile__num">04</span>
  </section>

  <div class="brand-tile">
    <span class="brand-tile__mark"></span>
    <span class="brand-tile__name">Tavrin Foods Packing</span>
  </div>

  <section class="tile tile--process">
    <svg class="tile__icon" style="left:195px;top:40px" width="140" height="140" viewBox="0 0 140 140">
      <circle cx="70" cy="70" r="30" stroke-dasharray="8 6" stroke-width="12"/>
      <circle cx="70" cy="70" r="14"/>
      <path d="M20 40a58 58 0 0 1 70-30M120 100a58 58 0 0 1-70 30M90 10l-8-8M90 10l-10 6M50 130l8 8M50 130l10-6"/>
    </svg>
    <h2 class="tile__title">Process<br>Control</h2>
    <span class="tile__num">05</span>
  </section>

  <aside class="side-band side-band--right"><span>OUR 5 TO DRIVE</span></aside>
</main>
</body>
</html>
```